Web tool bar Project

I'm open to paying more if the quality of the bar is very good... if you feel the scope of the project does not match budget..... please quote me.

I need someone to re-design my web tool bar.

In the first attachment you can see a black tool bar (fig1). This is my old design. I want this to be the template as it shows what the text will say and where the buttons will be placed.

For the new tool bar:
-I would like the it to be white in colour (like fig.2)
-I would like the buttons to also be white. But the buttons must stand out so the designer should use the right shading to make the buttons stand out.
-The bar needs to be the quality of the bar in fig.2 (very good quality). I have had many designs done for this but no designer seems to be good enough to get the right quality.
-The text in the white boxes on the new bar should be the colours shown above the buttons next to fig.1 (blue, green, red, yellow, purple & orange).

Finally please put the logo attached (DV) at the end of the bar on the right where it says logo. The logo should blend in well with the bar as it has white in it also.

Please take note of fig.2 it is good quality with sharp edges I would like the same quality.

Any further questions please ask?

Requirements
Must have
• Quality!

```html
<!DOCTYPE html>
<html lang="en">
<head>
<meta charset="utf-8">
<title>Toolbar Button Variations</title>
<link href="https://fonts.googleapis.com/css2?family=Arimo:wght@700&family=Poppins:wght@600&display=swap" rel="stylesheet">
<style>
  :root {
    --bg: #ffffff;
    --ink: #111111;
    --green: #2fd12f;
    --red: #e8303c;
    --yellow: #e3dc00;
    --purple: #c22cc2;
    --orange: #f7901e;
    --blue: #1b98d8;
    --arrow: #1440e0;
    --btn-top: #ffffff;
    --btn-bottom: #eceff1;
  }
  html, body {
    margin: 0;
    padding: 0;
    width: 1200px;
    height: 332px;
    overflow: hidden;
    background: var(--bg);
  }
  .canvas {
    position: relative;
    width: 1200px;
    height: 332px;
  }
  .heading {
    position: absolute;
    left: 0;
    width: 1210px;
    top: 24px;
    margin: 0;
    text-align: center;
    font: 700 20px "Arimo", Arial, sans-serif;
    color: var(--ink);
  }
  .btn {
    position: absolute;
    height: 48px;
    box-sizing: border-box;
    border: 1.5px solid var(--c);
    border-radius: 24px;
    background: linear-gradient(to bottom, var(--btn-top) 0%, #f9fafb 50%, var(--btn-bottom) 100%);
    box-shadow: inset 0 -3px 6px rgba(0,0,0,0.06), 0 2px 3px rgba(0,0,0,0.08);
    display: flex;
    align-items: center;
    padding-left: 9px;
    gap: 6px;
    font: 600 19px "Poppins", "Century Gothic", sans-serif;
    color: var(--c);
    white-space: nowrap;
    letter-spacing: -0.2px;
  }
  .btn svg { width: 28px; height: 28px; flex: none; fill: var(--c); }
  .btn .label { text-shadow: 1px 1px 1px rgba(0,0,0,0.18); }
  .btn.deep .label { text-shadow: 2px 2px 3px rgba(0,0,0,0.38); }
  .btn.deep svg { filter: drop-shadow(1px 1px 1px rgba(0,0,0,0.3)); }
  .btn.soft { background: linear-gradient(to bottom, #ffffff 0%, #f1f1f1 100%); box-shadow: inset 0 -6px 10px rgba(0,0,0,0.09); }

  .green { --c: var(--green); }
  .red { --c: var(--red); }
  .yellow { --c: var(--yellow); }
  .purple { --c: var(--purple); }
  .orange { --c: var(--orange); }
  .blue { --c: var(--blue); }

  .brand-tile {
    position: absolute;
    width: 46px;
    height: 48px;
    box-sizing: border-box;
    border-radius: 6px;
    background: var(--blue);
    display: flex;
    align-items: center;
    justify-content: center;
    font: 600 18px "Poppins", "Century Gothic", sans-serif;
    color: #ffffff;
  }

  .note {
    position: absolute;
    left: 375px;
    top: 274px;
    margin: 0;
    font: 700 19px/23px "Arimo", Arial, sans-serif;
    color: var(--ink);
  }
  .pointer { position: absolute; width: 36px; height: 44px; fill: var(--arrow); }
</style>
</head>
<body>
<div class="canvas">
  <svg width="0" height="0" style="position:absolute" aria-hidden="true">
    <defs>
      <symbol id="icon-check" viewBox="0 0 28 28">
        <path d="M4 6h14v3H7v14h14v-7h3v10H4z"/>
        <path d="M8 13l3-3 4 4 10-11 3 3-13 14z"/>
      </symbol>
      <symbol id="icon-person" viewBox="0 0 28 28">
        <circle cx="14" cy="8" r="6"/>
        <path d="M3 26c0-7 5-11 11-11s11 4 11 11z"/>
      </symbol>
      <symbol id="icon-feed" viewBox="0 0 28 28">
        <circle cx="7" cy="21" r="3.5"/>
        <path d="M3.5 11a13.5 13.5 0 0 1 13.5 13.5h-4A9.5 9.5 0 0 0 3.5 15z"/>
        <path d="M3.5 3a21.5 21.5 0 0 1 21.5 21.5h-4A17.5 17.5 0 0 0 3.5 7z"/>
      </symbol>
      <symbol id="icon-mail" viewBox="0 0 28 28">
        <path d="M2 6h24v3L14 16 2 9z"/>
        <path d="M2 11.5l12 7 12-7V23H2z"/>
      </symbol>
      <symbol id="icon-book" viewBox="0 0 28 28">
        <path d="M9 4h17l-7 18H3z"/>
        <path d="M3 22h16l-1 3H4a2 2 0 0 1-1-3z" opacity="0.75"/>
        <path d="M11 8h11l-0.8 2H10.2z" fill="#fff"/>
      </symbol>
      <symbol id="icon-login" viewBox="0 0 28 28">
        <circle cx="13" cy="8" r="6"/>
        <path d="M2 26c0-7 5-11 11-11 2 0 4 .5 5.5 1.5L12 26z"/>
        <path d="M14 26l8-9 3 3-8 9z"/>
      </symbol>
    </defs>
  </svg>

  <h1 class="heading">Here are a few variations in shading and drop shadowing</h1>

  <!-- Row 1 -->
  <div class="btn green" style="left:19px;top:76px;width:158px"><svg><use href="#icon-check"/></svg><span class="label">Check-In</span></div>
  <div class="btn red" style="left:190px;top:76px;width:337px"><svg><use href="#icon-person"/></svg><span class="label">Online Friends at Circlenet</span></div>
  <div class="btn yellow" style="left:539px;top:76px;width:213px"><svg><use href="#icon-feed"/></svg><span class="label">Lounge Feeds</span></div>
  <div class="btn purple" style="left:764px;top:76px;width:161px"><svg><use href="#icon-mail"/></svg><span class="label">Messages</span></div>
  <div class="btn orange" style="left:937px;top:76px;width:181px"><svg><use href="#icon-book"/></svg><span class="label">Scrapbook</span></div>
  <div class="brand-tile" style="left:1144px;top:76px">DV</div>

  <!-- Row 2 -->
  <div class="btn green deep" style="left:19px;top:135px;width:158px"><svg><use href="#icon-check"/></svg><span class="label">Check-In</span></div>
  <div class="btn red deep" style="left:190px;top:135px;width:337px"><svg><use href="#icon-person"/></svg><span class="label">Online Friends at Circlenet</span></div>
  <div class="btn yellow deep" style="left:539px;top:135px;width:213px"><svg><use href="#icon-feed"/></svg><span class="label">Lounge Feeds</span></div>
  <div class="btn purple deep" style="left:764px;top:135px;width:161px"><svg><use href="#icon-mail"/></svg><span class="label">Messages</span></div>
  <div class="btn orange deep" style="left:937px;top:135px;width:181px"><svg><use href="#icon-book"/></svg><span class="label">Scrapbook</span></div>
  <div class="brand-tile" style="left:1144px;top:135px">DV</div>

  <!-- Row 3 -->
  <div class="btn blue" style="left:19px;top:202px;width:278px"><svg><use href="#icon-login"/></svg><span class="label">Dove Valley Login</span></div>
  <div class="btn green soft" style="left:329px;top:202px;width:158px"><svg><use href="#icon-check"/></svg><span class="label">Check-In</span></div>
  <div class="btn yellow soft" style="left:539px;top:198px;width:213px"><svg><use href="#icon-feed"/></svg><span class="label">Lounge Feeds</span></div>

  <!-- Row 4 -->
  <div class="btn blue deep" style="left:19px;top:261px;width:278px"><svg><use href="#icon-login"/></svg><span class="label">Dove Valley Login</span></div>

  <!-- Notes -->
  <svg class="pointer" style="left:324px;top:264px" viewBox="0 0 36 44"><polygon points="30,0 34,26 26,20 8,44 0,38 18,14 10,8"/></svg>
  <svg class="pointer" style="left:730px;top:262px" viewBox="0 0 36 44"><polygon points="6,0 26,8 18,14 36,38 28,44 10,20 2,26"/></svg>
  <p class="note">These 2 colours maybe too light,<br>suggest darker colours or outline</p>
</div>
</body>
</html>
```